Surface Protection company needs cards

We are a New Zealand company that will apply nanotechnology coatings on surfaces to prevent growth and spread of bacteria, viruses, mold etc with a sprayer. We deal with large corporates, airlines, hospitals and schools so we are after a new modern, simple and clean look that will have great visual impact.
We a company that is focused on prevention and protection.

Company name, Vela Shield

Subtext, Antimicrobial Surface Protection

Logo, VS

Target Market(s)

Hospitals, Transport agencies, Airlines, Corporate entities

Contact Information for Business Card

Company name, VelaShield
Logo, VS

Gareth Tolley
velashieldnz@postbox.example
+64219305562
www.velashield.example.nz

Requirements
Must have
• Simple clean look.
Nice to have
• We apply nano coatings so try and incorporate this into a theme somehow

```html
<!DOCTYPE html>
<html lang="en">
<head>
<meta charset="utf-8">
<title>Vela Shield – Business Cards</title>
<link href="https://fonts.googleapis.com/css2?family=Josefin+Sans:wght@400;700&family=Poppins:wght@600&display=swap" rel="stylesheet">
<style>
  :root {
    --page-bg: #e6f0fb;
    --navy: #081a36;
    --white: #ffffff;
    --paper: #f4f7fc;
    --paper-shade: #e9edf4;
    --molecule: rgba(40, 90, 130, 0.18);
    --shadow: rgba(90, 120, 170, 0.22);
  }
  * { margin: 0; padding: 0; box-sizing: border-box; }
  html, body {
    width: 1135px; height: 1200px; overflow: hidden;
    background: var(--page-bg);
  }
  body { position: relative; font-family: "Josefin Sans", sans-serif; }

  /* Front card */
  .card-front {
    position: absolute; left: 79px; top: 27px; width: 977px; height: 559px;
    background: var(--white);
    box-shadow: 0 10px 30px var(--shadow);
  }
  .card-front__panel {
    position: absolute; left: 35px; top: 30px; width: 908px; height: 499px;
    background: var(--navy); overflow: hidden;
  }
  .molecule-field {
    position: absolute; inset: 0;
    background:
      radial-gradient(circle at 36% 13%, var(--molecule) 0, transparent 62px),
      radial-gradient(circle at 60% 13%, var(--molecule) 0, transparent 42px),
      radial-gradient(circle at 96% 9%, var(--molecule) 0, transparent 65px),
      radial-gradient(circle at 1% 40%, var(--molecule) 0, transparent 55px),
      radial-gradient(circle at 97% 51%, var(--molecule) 0, transparent 42px),
      radial-gradient(circle at 58% 84%, var(--molecule) 0, transparent 20px),
      radial-gradient(circle at 30% 95%, var(--molecule) 0, transparent 42px),
      radial-gradient(circle at 94% 93%, var(--molecule) 0, transparent 58px);
  }
  .brand-mark {
    position: absolute; border-radius: 50%;
  }
  .card-front .brand-mark {
    left: 401px; top: 159px; width: 106px; height: 106px; background: var(--white);
  }
  .brand-name {
    position: absolute; left: 0; right: 0; text-align: center;
    font-weight: 700; font-variant: small-caps; letter-spacing: 2px; line-height: 1;
  }
  .card-front .brand-name {
    top: 280px; font-size: 38px; color: var(--white);
  }
  .tagline {
    position: absolute; left: 0; right: 0; text-align: center;
    font-variant: small-caps; letter-spacing: 2px; line-height: 1;
  }
  .card-front .tagline {
    top: 319px; font-size: 23px; font-weight: 400; color: var(--white);
  }

  /* Back card */
  .card-back {
    position: absolute; left: 80px; top: 608px; width: 976px; height: 565px;
    box-shadow: 0 10px 30px var(--shadow);
    display: flex;
  }
  .card-back__contact {
    width: 488px; height: 100%; background: var(--navy); position: relative;
  }
  .person-name {
    position: absolute; left: 62px; top: 92px;
    font-size: 41px; color: var(--white); font-variant: small-caps;
    letter-spacing: 2px; line-height: 1;
  }
  .person-name__first { font-weight: 700; }
  .person-name__last { font-weight: 400; }
  .person-name__rule {
    position: absolute; left: 64px; top: 143px; width: 55px; height: 3px;
    background: var(--white); border-radius: 2px;
  }
  .contact-list { list-style: none; position: absolute; left: 62px; top: 302px; }
  .contact-item {
    display: flex; align-items: center; height: 38px; margin-bottom: 34px;
  }
  .contact-item__icon { width: 38px; height: 38px; flex: none; }
  .contact-item__text {
    margin-left: 9px;
    font-family: "Poppins", sans-serif; font-weight: 600;
    font-size: 12.5px; letter-spacing: 1.6px; color: var(--white);
    text-transform: uppercase;
  }

  .card-back__brand {
    flex: 1; position: relative;
    background: radial-gradient(ellipse at 40% 40%, var(--paper) 0%, var(--paper-shade) 100%);
  }
  .card-back__brand .brand-mark {
    left: 203px; top: 207px; width: 62px; height: 62px; background: var(--navy);
  }
  .card-back__brand .brand-name {
    top: 284px; font-size: 53px; color: var(--navy);
  }
  .card-back__brand .tagline {
    top: 344px; font-size: 18px; font-weight: 700; color: var(--navy);
  }
</style>
</head>
<body>

<section class="card-front">
  <div class="card-front__panel">
    <div class="molecule-field" role="img" aria-label="Faint nano-molecule sphere pattern across the navy background"></div>
    <div class="brand-mark"></div>
    <div class="brand-name">Vela Shield</div>
    <div class="tagline">Antimicrobial&nbsp; Surface&nbsp; Protection</div>
  </div>
</section>

<section class="card-back">
  <div class="card-back__contact">
    <h1 class="person-name"><span class="person-name__first">Gareth</span> <span class="person-name__last">Tolley</span></h1>
    <div class="person-name__rule"></div>
    <ul class="contact-list">
      <li class="contact-item">
        <svg class="contact-item__icon" viewBox="0 0 38 38" aria-hidden="true">
          <circle cx="19" cy="19" r="19" fill="#fff"/>
          <rect x="9" y="12" width="20" height="14" fill="none" stroke="#081a36" stroke-width="2.2"/>
          <path d="M9 12 L19 20 L29 12 M9 26 L16 19 M29 26 L22 19" fill="none" stroke="#081a36" stroke-width="2"/>
        </svg>
        <span class="contact-item__text">velashieldnz@postbox.example</span>
      </li>
      <li class="contact-item">
        <svg class="contact-item__icon" viewBox="0 0 38 38" aria-hidden="true">
          <circle cx="19" cy="19" r="19" fill="#fff"/>
          <circle cx="19" cy="19" r="11" fill="none" stroke="#081a36" stroke-width="2.4"/>
          <path d="M8 19 H30 M19 8 C13 14 13 24 19 30 C25 24 25 14 19 8" fill="none" stroke="#081a36" stroke-width="1.8"/>
        </svg>
        <span class="contact-item__text">www.velashield.example.nz</span>
      </li>
      <li class="contact-item">
        <svg class="contact-item__icon" viewBox="0 0 38 38" aria-hidden="true">
          <circle cx="19" cy="19" r="19" fill="#fff"/>
          <path d="M14 9 L18 14 L15.5 17 C17 21 19 23 22 24.5 L25 22 L30 26 L27 30 C18 30 8 20 9 12 Z" fill="#081a36"/>
        </svg>
        <span class="contact-item__text">+64219305562</span>
      </li>
    </ul>
  </div>
  <div class="card-back__brand">
    <div class="brand-mark"></div>
    <div class="brand-name">Vela Shield</div>
    <div class="tagline">Antimicrobial Surface Protection</div>
  </div>
</section>

</body>
</html>
```